Smart Election Management System

At this point, ensuring the designers understand the project scope is essential for us. Thus, a web design for an interactive prototype system. Users should be able to navigate through the system to review political election results on a dashboard. The system should provide at least the following options:

President (Maps by states or provinces, and municipalities)
Senate (Map by senatorial districts)
House (Map by representative districts)
Governor (Maps by states or provinces and municipalities)
Mayor (Maps by municipalities)

Each option should display its dashboard, including a map with election results, election results forecast, turnover stats, and related graphics.

These specifications provide a comprehensive outline for developing an interactive country map system that allows users to explore election statistics, including voter turnovers, results, and forecasts. It includes country and language selection, configuration options for political parties, dashboards, previous election comparisons, turnover election day timeline, and data collection screens.
1. Country and Language Selection:
o The system should allow users to select a country from the American continent, including Caribbean countries.
o Provide options for the preferred language (Spanish, English, and Portuguese).
o Dynamically adjust the content and language based on the user's selection.
2. Interactive Map:
o Include an interactive map of the selected country.
o Users can explore election statistics by region, province, or other administrative divisions.
o Allow users to click on a region or division to view specific election statistics for that area.
3. Configuration Screen:
o Provide a configuration screen accessible to administrators for setting up the system.
o Allow administrators to define up to 5 political parties:
 Fields to specify the party's acronym or short name, symbol, and color for visual representation.
 Include fields to define the party's full name and an event description (e.g., General Election, Primary Election, etc.).
o Save the configuration settings to ensure consistency across the system.
4. Dashboard Navigation:
o Implement a user-friendly dashboard for easy navigation and access to different election races and statistics.
o Include clear menus or tabs to select the desired race (presidential, congress, or mayor) and related statistics.
5. Voter Turnover Statistics:
o Display visualizations and metrics for tracking voter turnovers:
 Total voter turnover for the current election.
 Breakdowns of voter turnovers by gender, age, and party affiliation.
 Comparison of voter turnovers between the previous election and the current election.
 Turnover election day timeline by hours, showing the number of votes cast at different times throughout the election day.
6. Election Results:
o Show election results for different races: presidential, congress, and mayor.
o Provide visualizations and metrics for the following:
 Total votes by political party or candidate.
 Comparison of previous election results and current election results.
 Election results timeline, demonstrating the progression of results over time.
7. Election Result Forecasts:
o Provide forecasted election results for each race.
o Display visualizations and metrics for the following:
 Total votes by political party or candidate in the presidential, congress, and mayoral races.
 Allow users to explore different scenarios or predictions based on available data.
8. Previous Elections Comparison:
o Include a section comparing the current election's statistics with previous elections.
o Display visualizations and metrics to demonstrate changes in voter turnovers, results, and other relevant metrics.
9. Turnout Data Collection Screens:
o Develop data collection screens for gathering information at polling places.
o Design intuitive and user-friendly interfaces for collecting voter turnout data, including age, gender, and party affiliation.

Target Market(s)

Political parties, press

Industry/Entity Type

Political campaigns

Number of Pages Required

5+ page

Requirements
Must have
• Interactive funcionality

```html
<!DOCTYPE html>
<html lang="en">
<head>
<meta charset="utf-8">
<title>Smart Election Management System</title>
<link href="https://fonts.googleapis.com/css2?family=Oswald:wght@500;600&family=Roboto:wght@400;500;700&display=swap" rel="stylesheet">
<style>
:root{
  --ink:#111;
  --muted:#555;
  --blue:#1a5cff;
  --blue-mid:#2f8af5;
  --red:#ff4a3f;
  --red-deep:#e8391f;
  --green:#1f8a1f;
  --yellow:#ffd21a;
  --cyan:#aef0ef;
  --brown:#d08a4a;
  --navy:#0b3a7a;
  --nav-bg:#ececec;
  --panel-bg:#f5f5f5;
  --line:#c9c9c9;
  --white:#fff;
}
*{box-sizing:border-box;margin:0;padding:0}
html,body{width:1200px;height:3263px;overflow:hidden;background:var(--white);color:var(--ink);font-family:"Roboto",Arial,sans-serif}
.page{position:relative;width:1200px;height:3263px}
.abs{position:absolute}

/* header */
.brand{left:84px;top:70px;display:flex;align-items:center;gap:12px}
.brand-mark{width:26px;height:26px;background:var(--ink)}
.brand-name{font-family:"Oswald",sans-serif;font-weight:600;font-size:38px;color:var(--ink)}
.title-frame{left:322px;top:49px;width:794px;height:140px;border:4px solid var(--ink);padding:6px}
.title-frame-inner{width:100%;height:100%;border:2px solid var(--ink);display:flex;align-items:center;justify-content:center;font-family:"Oswald",sans-serif;font-weight:600;font-size:50px;letter-spacing:.3px}

/* nav */
.main-nav{left:0;top:247px;width:1200px;height:70px;background:var(--nav-bg)}
.main-nav a{position:absolute;top:22px;font-size:21px;color:var(--ink);text-decoration:none;font-weight:500}
.submenu{left:71px;top:308px;width:308px;border:2px solid var(--line);background:var(--white)}
.submenu a{display:block;height:48px;line-height:46px;padding-left:18px;font-size:21px;font-weight:500;color:var(--ink);text-decoration:none;border-bottom:2px solid var(--line)}
.submenu a:last-child{border-bottom:0}

.lang{left:959px;top:352px;width:192px;height:229px;border:1px solid var(--line);background:var(--white);font-size:11px}
.lang-head{padding:10px 7px 8px;border-bottom:2px solid #b6c8ee;font-size:12px}
.lang ul{list-style:none;padding:10px 5px}
.lang li{display:flex;align-items:center;gap:8px;height:29px;padding-left:8px;font-weight:500;font-size:11px}
.lang li.active{background:#f0f0f0;border-radius:4px}
.flag{width:17px;height:11px;display:inline-block}

.section-title{left:0;width:1200px;text-align:center;font-family:"Oswald",sans-serif;font-weight:500;font-size:28px;letter-spacing:.5px}

/* scoreboard */
.portrait{width:93px;height:120px;border:2px solid var(--ink);background:linear-gradient(#f7f7f7,#cfcfcf)}
.score{font-family:"Oswald",sans-serif;font-size:44px;line-height:1}
.cand{font-family:"Oswald",sans-serif;font-size:28px;font-weight:500}
.win-bar{left:256px;top:872px;width:641px;height:22px;background:var(--red);border-radius:3px;overflow:hidden}
.win-bar span{display:block;width:365px;height:100%;background:var(--blue)}
.marker{left:576px;top:868px;width:2px;height:30px;background:var(--ink)}
.pct{font-size:17px;top:907px}
.divider{left:0;top:945px;width:1200px;height:4px;background:linear-gradient(90deg,#b8cdf5,#e9e0ea 50%,#f3b8c0)}

/* map panel */
.map-panel{left:0;top:949px;width:1200px;height:625px;background:var(--panel-bg)}
.legend-title{left:487px;top:998px;font-weight:700;font-size:18px}
.legend-sub{left:448px;top:1024px;font-size:10px;color:var(--muted)}
.swatch{width:21px;height:14px}
.swatch.hatch-b{background:repeating-linear-gradient(45deg,var(--blue) 0 3px,#cfe0ff 3px 5px)}
.swatch.hatch-r{background:repeating-linear-gradient(45deg,var(--red) 0 3px,#ffd6d2 3px 5px)}
.legend-tag{font-size:9px;color:var(--muted)}
.zoom{left:228px;top:1066px;width:32px;height:58px;background:var(--white);border:1px solid #ddd;font-weight:700;font-size:16px;text-align:center;line-height:29px}
.side-label{font-size:12px;font-weight:700}
.thumb{left:76px;width:110px;height:78px;border:1px solid #999;border-radius:4px;background:var(--white);overflow:hidden}
.thumb .art{height:58px}
.thumb .cap{font-family:"Oswald",sans-serif;font-size:11px;text-align:center;line-height:18px}
.us-map{left:275px;top:1066px;width:800px;height:505px;border-radius:40px 90px 30px 60px;background:linear-gradient(90deg,#2f6cf0 0%,#ff5a4f 35%,#ff5a4f 55%,#4a7ff0 72%,#ff5a4f 86%,#2f6cf0 100%)}

/* footer */
.footer{left:0;top:3205px;width:1200px;height:58px;background:var(--nav-bg);text-align:center;line-height:58px;font-size:12px}
</style>
</head>
<body>
<div class="page">

  <div class="abs brand"><span class="brand-mark"></span><span class="brand-name">Ballotline</span></div>
  <div class="abs title-frame"><div class="title-frame-inner">Smart Election Management System</div></div>

  <nav class="abs main-nav">
    <a style="left:82px" href="#">MAPS</a>
    <a style="left:202px" href="#">LIST OF PARTIES</a>
    <a style="left:411px" href="#">TRACK VOTER’S TURNOVER</a>
    <a style="left:740px" href="#">RESULTS FORECAST</a>
    <a style="left:979px" href="#">COMPARISONS</a>
  </nav>
  <div class="abs submenu">
    <a href="#">Map by States</a>
    <a href="#">Map by Senatorial Districts</a>
    <a href="#">Map by Provinces</a>
    <a href="#">Map by Municipalities</a>
  </div>

  <div class="abs lang">
    <div class="lang-head">Preferred Language</div>
    <ul>
      <li><span class="flag" style="background:linear-gradient(#000 0 33%,#d00 33% 66%,#fc0 66%)"></span>Deutschland</li>
      <li class="active"><span class="flag" style="background:linear-gradient(90deg,#0033a0 0 33%,#fff 33% 66%,#ef4135 66%)"></span>France</li>
      <li><span class="flag" style="background:linear-gradient(#0000 0 40%,#c8102e 40% 60%,#0000 60%),linear-gradient(90deg,#012169 0 42%,#c8102e 42% 58%,#012169 58%)"></span>United Kingdom</li>
      <li><span class="flag" style="background:linear-gradient(90deg,#169b62 0 33%,#fff 33% 66%,#ff883e 66%)"></span>Ireland</li>
      <li><span class="flag" style="background:linear-gradient(#ae1c28 0 33%,#fff 33% 66%,#21468b 66%)"></span>Netherlands</li>
      <li><span class="flag" style="background:linear-gradient(#ed2939 0 33%,#fff 33% 66%,#ed2939 66%)"></span>Österreich</li>
    </ul>
  </div>

  <h2 class="abs section-title" style="top:684px">MAP BY STATES</h2>

  <div class="abs portrait" style="left:148px;top:805px" role="img" aria-label="Candidate A portrait placeholder"></div>
  <div class="abs portrait" style="left:908px;top:805px" role="img" aria-label="Candidate B portrait placeholder"></div>
  <div class="abs score" style="left:256px;top:822px;color:var(--blue)">306</div>
  <div class="abs cand" style="left:334px;top:828px;color:var(--blue)">CANDIDATE A</div>
  <div class="abs" style="left:540px;top:834px;font-size:14px">270 to Win</div>
  <div class="abs" style="left:572px;top:851px;font-size:8px">▼</div>
  <div class="abs cand" style="left:676px;top:828px;color:var(--red-deep)">CANDIDATE B</div>
  <div class="abs score" style="left:834px;top:822px;color:var(--red-deep)">232</div>
  <div class="abs win-bar"><span></span></div>
  <div class="abs marker"></div>
  <div class="abs pct" style="left:256px"><b>51.3%</b>&nbsp;&nbsp;&nbsp;81,284,666</div>
  <div class="abs" style="left:537px;top:920px;font-size:12px;font-style:italic;color:var(--muted)">ⓘ What is this?</div>
  <div class="abs pct" style="left:747px">74,224,319&nbsp;&nbsp;&nbsp;<b>46.9%</b></div>
  <div class="abs divider"></div>

  <section class="abs map-panel"></section>
  <div class="abs legend-title">Projection</div>
  <div class="abs legend-sub">Updated 10:44 a.m. ET, May. 5</div>
  <div class="abs" style="left:615px;top:1001px;display:flex;gap:2px"><span class="swatch" style="background:var(--blue)"></span><span class="swatch hatch-b"></span></div>
  <div class="abs legend-tag" style="left:618px;top:1018px">Win&nbsp;&nbsp;&nbsp;Flip</div>
  <div class="abs" style="left:724px;top:1001px;display:flex;gap:2px"><span class="swatch" style="background:var(--red)"></span><span class="swatch hatch-r"></span></div>
  <div class="abs legend-tag" style="left:727px;top:1018px">Win&nbsp;&nbsp;&nbsp;Flip</div>

  <div class="abs zoom">+<br>-</div>

  <div class="abs side-label" style="left:76px;top:1102px">Maps</div>
  <div class="abs thumb" style="top:1119px"><div class="art" style="background:#e3e3e3" role="img" aria-label="Projection map thumbnail"></div><div class="cap">Newsdesk Projection</div></div>
  <div class="abs thumb" style="top:1201px"><div class="art" style="background:linear-gradient(90deg,#ff6a60,#5a8ef5)" role="img" aria-label="Size of lead map thumbnail"></div><div class="cap">Size of Lead</div></div>
  <div class="abs side-label" style="left:76px;top:1300px">Filters <span style="font-weight:400;font-size:8px;color:#bbb;border:1px solid #ddd;border-radius:6px;padding:0 5px">CLEAR</span></div>
  <div class="abs thumb" style="top:1318px"><div class="art" style="background:#fff8d6" role="img" aria-label="Battleground states outline thumbnail"></div><div class="cap">Battleground</div></div>
  <div class="abs thumb" style="top:1400px"><div class="art" style="background:linear-gradient(90deg,#ff6a60,#2f6cf0)" role="img" aria-label="Flipped seats map thumbnail"></div><div class="cap">Flipped Seats</div></div>

  <div class="abs us-map" role="img" aria-label="Interactive map of the country coloured by projected winner per state, blue for Candidate A and red for Candidate B, with state abbreviations"></div>

  <h2 class="abs section-title" style="top:1795px">RESULT STATISTICS</h2>

  <svg class="abs" style="left:240px;top:1895px" width="720" height="200" viewBox="0 0 720 200" font-family="Arial,sans-serif" font-size="12">
    <g fill="var(--navy)" font-weight="700" text-anchor="middle" font-size="12">
      <text x="100" y="20">10 days</text>
      <text x="264" y="20">2 days</text>
      <text x="429" y="20">1 day</text>
      <text x="596" y="12">RESULTS</text>
      <text x="596" y="25">(Camera)</text>
    </g>
    <g transform="translate(100,113)">
      <g transform="rotate(-90)" fill="none" stroke-width="63">
        <circle r="31.5" pathLength="100" stroke="var(--yellow)" stroke-dasharray="16.9 100"/>
        <circle r="31.5" pathLength="100" stroke="var(--cyan)" stroke-dasharray="13.1 100" stroke-dashoffset="-16.9"/>
        <circle r="31.5" pathLength="100" stroke="var(--blue-mid)" stroke-dasharray="26 100" stroke-dashoffset="-30"/>
        <circle r="31.5" pathLength="100" stroke="var(--red-deep)" stroke-dasharray="21.1 100" stroke-dashoffset="-56"/>
        <circle r="31.5" pathLength="100" stroke="var(--green)" stroke-dasharray="23 100" stroke-dashoffset="-77.1"/>
      </g>
      <circle r="63" fill="none" stroke="#555" stroke-width="1"/>
      <g text-anchor="middle" font-size="11">
        <text x="28" y="-26">16.9%</text><text x="42" y="8">13.1%</text><text x="6" y="42">26.0%</text><text x="-38" y="4">21.1%</text><text x="-22" y="-32">23.0%</text>
      </g>
      <g font-size="12"><text x="-75" y="-72">Small</text><text x="62" y="-50">MRV</text><text x="68" y="30">CV</text><text x="-20" y="78">LPF</text><text x="-100" y="2">DU</text></g>
    </g>
    <g transform="translate(264,113)">
      <g transform="rotate(-90)" fill="none" stroke-width="63">
        <circle r="31.5" pathLength="100" stroke="var(--yellow)" stroke-dasharray="20 100"/>
        <circle r="31.5" pathLength="100" stroke="var(--cyan)" stroke-dasharray="14.3 100" stroke-dashoffset="-20"/>
        <circle r="31.5" pathLength="100" stroke="var(--blue-mid)" stroke-dasharray="25.7 100" stroke-dashoffset="-34.3"/>
        <circle r="31.5" pathLength="100" stroke="var(--red-deep)" stroke-dasharray="22.9 100" stroke-dashoffset="-60"/>
        <circle r="31.5" pathLength="100" stroke="var(--green)" stroke-dasharray="17.1 100" stroke-dashoffset="-82.9"/>
      </g>
      <circle r="63" fill="none" stroke="#555" stroke-width="1"/>
      <g text-anchor="middle" font-size="11"><text x="27" y="-24">20.0%</text><text x="42" y="12">14.3%</text><text x="6" y="44">25.7%</text><text x="-38" y="6">22.9%</text><text x="-18" y="-32">17.1%</text></g>
      <g><text x="-72" y="-72">Small</text><text x="62" y="-50">MRV</text><text x="68" y="30">CV</text><text x="-20" y="78">LPF</text><text x="-96" y="2">DU</text></g>
    </g>
    <g transform="translate(429,113)">
      <g transform="rotate(-90)" fill="none" stroke-width="63">
        <circle r="31.5" pathLength="100" stroke="var(--yellow)" stroke-dasharray="22.4 100"/>
        <circle r="31.5" pathLength="100" stroke="var(--cyan)" stroke-dasharray="13.7 100" stroke-dashoffset="-22.4"/>
        <circle r="31.5" pathLength="100" stroke="var(--blue-mid)" stroke-dasharray="25.2 100" stroke-dashoffset="-36.1"/>
        <circle r="31.5" pathLength="100" stroke="var(--red-deep)" stroke-dasharray="22.3 100" stroke-dashoffset="-61.3"/>
        <circle r="31.5" pathLength="100" stroke="var(--green)" stroke-dasharray="16.4 100" stroke-dashoffset="-83.6"/>
      </g>
      <circle r="63" fill="none" stroke="#555" stroke-width="1"/>
      <g text-anchor="middle" font-size="11"><text x="28" y="-22">22.4%</text><text x="40" y="16">13.7%</text><text x="3" y="44">25.2%</text><text x="-38" y="10">22.3%</text><text x="-18" y="-32">16.4%</text></g>
      <g><text x="-62" y="-68">Small</text><text x="62" y="-55">MRV</text><text x="68" y="30">CV</text><text x="-20" y="78">LPF</text><text x="-96" y="2">DU</text></g>
    </g>
    <g transform="translate(596,113)">
      <g transform="rotate(-90)" fill="none" stroke-width="63">
        <circle r="31.5" pathLength="100" stroke="var(--yellow)" stroke-dasharray="25.6 100"/>
        <circle r="31.5" pathLength="100" stroke="var(--brown)" stroke-dasharray="7.6 100" stroke-dashoffset="-25.6"/>
        <circle r="31.5" pathLength="100" stroke="var(--cyan)" stroke-dasharray="8.3 100" stroke-dashoffset="-33.2"/>
        <circle r="31.5" pathLength="100" stroke="var(--blue-mid)" stroke-dasharray="21.6 100" stroke-dashoffset="-41.5"/>
        <circle r="31.5" pathLength="100" stroke="var(--red-deep)" stroke-dasharray="25.4 100" stroke-dashoffset="-63.1"/>
        <circle r="31.5" pathLength="100" stroke="var(--green)" stroke-dasharray="11.5 100" stroke-dashoffset="-88.5"/>
      </g>
      <circle r="63" fill="none" stroke="#555" stroke-width="1"/>
      <g text-anchor="middle" font-size="11"><text x="30" y="-22">25.6%</text><text x="44" y="12">7.6%</text><text x="32" y="34">8.3%</text><text x="-2" y="46">21.6%</text><text x="-38" y="4">25.4%</text><text x="-12" y="-38">11.5%</text></g>
      <g><text x="-64" y="-72">Small</text><text x="62" y="-58">MRV</text><text x="72" y="16">Others</text><text x="60" y="54">CV</text><text x="-20" y="78">LPF</text><text x="-96" y="2">DU</text></g>
    </g>
  </svg>

  <svg class="abs" style="left:240px;top:2090px" width="720" height="260" viewBox="0 0 720 260" font-family="Arial,sans-serif" font-size="10">
    <rect x="382" y="7" width="16" height="215" fill="#f7f3c6"/>
    <rect x="398" y="7" width="16" height="215" fill="#d8ead5"/>
    <rect x="23" y="7" width="652" height="215" fill="none" stroke="#888"/>
    <g stroke="#ddd" stroke-dasharray="2 3">
      <line x1="23" y1="29" x2="675" y2="29"/><line x1="23" y1="93" x2="675" y2="93"/><line x1="23" y1="158" x2="675" y2="158"/>
      <line x1="88" y1="7" x2="88" y2="222"/><line x1="252" y1="7" x2="252" y2="222"/><line x1="414" y1="7" x2="414" y2="222"/><line x1="577" y1="7" x2="577" y2="222"/>
    </g>
    <g fill="none" stroke-width="2">
      <polyline stroke="#2f7fe0" points="23,222 55,216 88,210 120,203 154,190 186,183 219,175 252,163 285,156 318,150 350,143 382,137 400,134 414,110 446,102 479,96 512,94 545,91 577,90 610,89 643,88 675,86"/>
      <polyline stroke="#ff6a20" points="23,222 55,218 88,213 120,207 154,196 186,190 219,182 252,172 285,166 318,160 350,155 382,150 400,148 414,124 446,107 479,97 512,91 545,85 577,82 610,78 643,73 675,68"/>
      <polyline stroke="#f0c000" points="23,222 55,219 88,215 120,209 154,200 186,194 219,186 252,177 285,170 318,164 350,159 382,154 400,152 414,132 446,114 479,100 512,92 545,86 577,82 610,77 643,72 675,66"/>
      <polyline stroke="#2a8a2a" points="23,222 55,219 88,216 120,212 154,206 186,203 219,199 252,194 285,190 318,187 350,184 382,181 400,180 414,164 446,158 479,157 512,156 545,155 577,155 610,154 643,154 675,153"/>
      <polyline stroke="#8ed6d6" points="23,222 55,220 88,218 120,215 154,210 186,207 219,203 252,198 285,195 318,192 350,189 382,187 400,186 414,172 446,166 479,164 512,163 545,163 577,163 610,162 643,162 675,162"/>
    </g>
    <rect x="26" y="10" width="62" height="72" fill="#fff" stroke="#aaa"/>
    <g font-size="10">
      <line x1="30" y1="18" x2="46" y2="18" stroke="#f0c000" stroke-width="2"/><text x="50" y="21">MRV</text>
      <line x1="30" y1="32" x2="46" y2="32" stroke="#ff6a20" stroke-width="2"/><text x="50" y="35">DU</text>
      <line x1="30" y1="46" x2="46" y2="46" stroke="#2f7fe0" stroke-width="2"/><text x="50" y="49">LPF</text>
      <line x1="30" y1="60" x2="46" y2="60" stroke="#8ed6d6" stroke-width="2"/><text x="50" y="63">CV</text>
      <line x1="30" y1="74" x2="46" y2="74" stroke="#2a8a2a" stroke-width="2"/><text x="50" y="77">Small</text>
    </g>
    <text x="360" y="73" font-size="12">election days</text>
    <g font-size="9"><text x="678" y="32">900000</text><text x="678" y="96">600000</text><text x="678" y="161">300000</text></g>
    <text transform="translate(14,160) rotate(-90)" font-size="11">total tweets</text>
    <g text-anchor="middle" font-size="11">
      <text x="88" y="233">16</text><text x="88" y="245">Feb</text>
      <text x="252" y="233">21</text><text x="252" y="245">Feb</text>
      <text x="414" y="233">26</text><text x="414" y="245">Feb</text>
      <text x="577" y="233">03</text><text x="577" y="245">Mar</text>
    </g>
  </svg>

  <h2 class="abs section-title" style="top:2540px">VOTER TURNOVER BY GENDER</h2>

  <svg class="abs" style="left:310px;top:2655px" width="570" height="355" viewBox="0 0 570 355" font-family="Arial,sans-serif" font-size="7">
    <text x="285" y="14" text-anchor="middle" font-size="10">Voter Turnout by Sex and Age, Sample National Presidential Election.</text>
    <text x="285" y="28" text-anchor="middle" font-size="7">Source: Civic Data Office.</text>
    <polygon points="55,50 540,50 540,305 55,305" fill="#fafafa" stroke="#bbb"/>
    <g stroke="#e3e3e3">
      <line x1="55" y1="82" x2="540" y2="82"/><line x1="55" y1="116" x2="540" y2="116"/><line x1="55" y1="151" x2="540" y2="151"/><line x1="55" y1="185" x2="540" y2="185"/><line x1="55" y1="220" x2="540" y2="220"/><line x1="55" y1="254" x2="540" y2="254"/><line x1="55" y1="288" x2="540" y2="288"/>
    </g>
    <g text-anchor="end" fill="#333">
      <text x="26" y="51">80.0</text><text x="26" y="85">70.0</text><text x="26" y="120">60.0</text><text x="26" y="154">50.0</text><text x="26" y="189">40.0</text><text x="26" y="223">30.0</text><text x="26" y="258">20.0</text><text x="26" y="292">10.0</text><text x="26" y="326">0.0</text>
    </g>
    <polygon points="30,323 55,305 540,305 515,323" fill="#ddd" stroke="#aaa"/>
    <rect x="132" y="64" width="8" height="6" fill="var(--navy)"/><text x="144" y="70">male</text>
    <rect x="132" y="74" width="8" height="6" fill="var(--red-deep)"/><text x="144" y="80">female</text>
    <g>
      <rect x="48" y="130" width="17" height="192" fill="var(--navy)"/><rect x="70" y="114" width="17" height="208" fill="var(--red-deep)"/>
      <rect x="108" y="181" width="17" height="141" fill="var(--navy)"/><rect x="130" y="158" width="17" height="164" fill="var(--red-deep)"/>
      <rect x="168" y="170" width="17" height="152" fill="var(--navy)"/><rect x="190" y="140" width="17" height="182" fill="var(--red-deep)"/>
      <rect x="228" y="140" width="17" height="182" fill="var(--navy)"/><rect x="250" y="123" width="17" height="199" fill="var(--red-deep)"/>
      <rect x="288" y="113" width="17" height="209" fill="var(--navy)"/><rect x="310" y="99" width="17" height="223" fill="var(--red-deep)"/>
      <rect x="348" y="93" width="17" height="229" fill="var(--navy)"/><rect x="370" y="82" width="17" height="240" fill="var(--red-deep)"/>
      <rect x="408" y="80" width="17" height="242" fill="var(--navy)"/><rect x="430" y="81" width="17" height="241" fill="var(--red-deep)"/>
      <rect x="468" y="79" width="17" height="243" fill="var(--navy)"/><rect x="490" y="105" width="17" height="217" fill="var(--red-deep)"/>
    </g>
    <g text-anchor="middle" font-size="6">
      <text x="56" y="126">55.7</text><text x="78" y="110">60.4</text><text x="116" y="177">41.0</text><text x="138" y="154">47.7</text>
      <text x="176" y="166">44.0</text><text x="198" y="136">52.9</text><text x="236" y="136">52.7</text><text x="258" y="119">57.6</text>
      <text x="296" y="109">60.5</text><text x="318" y="95">64.7</text><text x="356" y="89">66.3</text><text x="378" y="78">69.7</text>
      <text x="416" y="76">70.1</text><text x="438" y="77">70.0</text><text x="476" y="75">70.3</text><text x="498" y="101">62.9</text>
    </g>
    <g text-anchor="middle" font-size="6" fill="#333">
      <text x="2" y="340" text-anchor="start">Total 18 years and over</text><text x="120" y="333">18 to 24 years</text><text x="180" y="340">25 to 34 years</text>
      <text x="240" y="333">35 to 44 years</text><text x="300" y="340">45 to 54 years</text><text x="360" y="333">55 to 64 years</text>
      <text x="420" y="340">65 to 74 years</text><text x="480" y="333">75 years and over</text>
    </g>
  </svg>

  <footer class="abs footer">Copyright&nbsp; Smart Election Management System</footer>
</div>
</body>
</html>
```